Harlow Company Core Values

We are looking for an updated appearance to our Core Values with the addition of some descriptors to share with new hires, employees, and potential candidates

Requirements
Must have
• Core values and core value descriptors

```html
<!DOCTYPE html>
<html lang="en">
<head>
<meta charset="utf-8">
<title>Harlow Company – Our Core Values</title>
<link href="https://fonts.googleapis.com/css2?family=Montserrat:wght@300;400;500;600&display=swap" rel="stylesheet">
<style>
  :root {
    --backdrop: #9aa6b2;
    --paper: #ffffff;
    --brand-red: #a61c2b;
    --ink: #1c1c1c;
  }
  html, body {
    margin: 0;
    padding: 0;
    width: 1200px;
    height: 1200px;
    overflow: hidden;
    background: var(--backdrop);
    font-family: "Montserrat", Arial, sans-serif;
  }
  .sheet {
    position: absolute;
    left: 160px;
    top: 30px;
    width: 880px;
    height: 1140px;
    background: var(--paper);
  }
  .brand {
    position: absolute;
    left: 60px;
    top: 60px;
  }
  .brand-name {
    display: block;
    font-size: 22px;
    font-weight: 500;
    color: var(--ink);
    line-height: 1.1;
  }
  .brand-tagline {
    display: block;
    font-size: 10px;
    font-weight: 500;
    color: var(--ink);
    margin-top: 4px;
    letter-spacing: 0.3px;
  }
  .value {
    position: absolute;
    width: 230px;
    margin-left: -115px;
    text-align: center;
  }
  .value-badge {
    display: block;
    width: 170px;
    height: 170px;
    margin: 0 auto 14px;
  }
  .value-title {
    font-size: 17px;
    font-weight: 500;
    color: var(--ink);
    margin: 0 0 4px;
  }
  .value-points {
    list-style: none;
    margin: 0;
    padding: 0;
    font-size: 14px;
    line-height: 1.3;
    color: var(--brand-red);
  }
  .headline {
    position: absolute;
    left: 340px;
    top: 440px;
    margin: 0;
    font-size: 56px;
    font-weight: 300;
    line-height: 1.12;
    color: var(--ink);
    letter-spacing: 1px;
  }
  .headline span { display: block; }
  .headline .indent { padding-left: 22px; }
</style>
</head>
<body>
  <main class="sheet">
    <div class="brand">
      <span class="brand-name">Harlow Company</span>
      <span class="brand-tagline">Moving Work Forward Every Day</span>
    </div>

    <section class="value" style="left:330px; top:130px;">
      <svg class="value-badge" viewBox="0 0 170 170" role="img" aria-label="Icon of a handshake forming a heart"><circle cx="85" cy="85" r="85" fill="var(--brand-red)"/></svg>
      <h2 class="value-title">Respect Everyone</h2>
      <ul class="value-points"><li>Be kind</li><li>Embrace each other's differences</li><li>Healthy conflict</li></ul>
    </section>

    <section class="value" style="left:570px; top:130px;">
      <svg class="value-badge" viewBox="0 0 170 170" role="img" aria-label="Icon of two hands holding a heart"><circle cx="85" cy="85" r="85" fill="var(--brand-red)"/></svg>
      <h2 class="value-title">Take Care</h2>
      <ul class="value-points"><li>Be safe</li><li>Be well</li><li>Look out for others</li></ul>
    </section>

    <section class="value" style="left:170px; top:400px;">
      <svg class="value-badge" viewBox="0 0 170 170" role="img" aria-label="Icon of an award ribbon with a star"><circle cx="85" cy="85" r="85" fill="var(--brand-red)"/></svg>
      <h2 class="value-title">Aim for excellence</h2>
      <ul class="value-points"><li>Learn from our mistakes</li><li>Getting a little better everyday</li><li>Life long Learner</li></ul>
    </section>

    <section class="value" style="left:710px; top:400px;">
      <svg class="value-badge" viewBox="0 0 170 170" role="img" aria-label="Icon of balanced scales of justice"><circle cx="85" cy="85" r="85" fill="var(--brand-red)"/></svg>
      <h2 class="value-title">Act Ethically</h2>
      <ul class="value-points"><li>Respect</li><li>Doing the right thing, even when no one is looking</li><li>Understand what matters to others</li></ul>
    </section>

    <h1 class="headline"><span>OUR</span><span class="indent">CORE</span><span>VALUES</span></h1>

    <section class="value" style="left:215px; top:720px;">
      <svg class="value-badge" viewBox="0 0 170 170" role="img" aria-label="Icon of people exchanging messages"><circle cx="85" cy="85" r="85" fill="var(--brand-red)"/></svg>
      <h2 class="value-title">Communicate</h2>
      <ul class="value-points"><li>Listen with intent</li><li>Ask questions</li><li>Think about delivery of message</li></ul>
    </section>

    <section class="value" style="left:690px; top:720px;">
      <svg class="value-badge" viewBox="0 0 170 170" role="img" aria-label="Icon of a light bulb with a brain inside"><circle cx="85" cy="85" r="85" fill="var(--brand-red)"/></svg>
      <h2 class="value-title">Work Smart</h2>
      <ul class="value-points"><li>Choose priorities</li><li>Focus</li><li>Seek to understand</li></ul>
    </section>

    <section class="value" style="left:450px; top:830px;">
      <svg class="value-badge" viewBox="0 0 170 170" role="img" aria-label="Icon of a heart with a flame"><circle cx="85" cy="85" r="85" fill="var(--brand-red)"/></svg>
      <h2 class="value-title">Share your passion</h2>
      <ul class="value-points"><li>Enjoy what you do</li><li>Help others</li><li>Positive outlook</li></ul>
    </section>
  </main>
</body>
</html>
```